Daily Deals Website Needs a Landing Page (Home Page will act as the landing page)

We need a landing page for a daily deals website that will act as the home page. We have attached the wire frame and logo for reference. Open to creative ideas and suggestions as long as the main elements of the wireframe are incorporated in the design. Need a very simplistic design approach like Vorplex's search page. (www.vorplex.com) . Very clean and distinct CTA's.

Target Market(s)

Customers looking for deals on everyday use items

Font styles to use
Sans Serif

Requirements
Must have
• clean design, lots of white space and strong CTA .
Nice to have
• need a clean design overall. Strong CTA
Should not have
• Cluttered look. Too many colors, keep it simple

```html
<!DOCTYPE html>
<html lang="en">
<head>
<meta charset="UTF-8">
<title>Linqora — Daily Deals</title>
<link href="https://fonts.googleapis.com/css2?family=Roboto:wght@400;700;900&display=swap" rel="stylesheet">
<style>
  :root {
    --bg: #f4f4f4;
    --bg-sheen: #fbfbfb;
    --navy: #233a96;
    --green: #6cc552;
    --ink: #141414;
    --body-ink: #2a2a2a;
    --footer-bg: #dcdcdc;
    --footer-ink: #555555;
    --white: #ffffff;
  }
  * { box-sizing: border-box; margin: 0; padding: 0; }
  html, body { width: 1200px; height: 936px; overflow: hidden; }
  body {
    position: relative;
    font-family: "Roboto", Arial, sans-serif;
    background: linear-gradient(135deg, var(--bg) 0%, var(--bg-sheen) 30%, var(--bg) 45%, var(--bg-sheen) 65%, var(--bg) 100%);
  }
  .brand {
    position: absolute; top: 88px; left: 0; width: 1200px;
    text-align: center;
    font-size: 72px; font-weight: 900; letter-spacing: 2px;
    color: var(--navy); line-height: 1;
  }
  .tagline {
    position: absolute; top: 196px; left: 0; width: 1200px;
    text-align: center; font-size: 15px; font-weight: 700; color: var(--ink);
  }
  .cta-button {
    position: absolute; left: 394px; width: 411px; height: 41px;
    background: var(--green); color: var(--white);
    font-size: 15px; font-weight: 700;
    display: flex; align-items: center; justify-content: center;
    text-decoration: none;
  }
  .cta-top { top: 244px; }
  .cta-bottom { top: 795px; }
  .deal-card { position: absolute; top: 337px; width: 457px; text-align: center; }
  .deal-left { left: 122px; }
  .deal-right { left: 617px; }
  .deal-visual { width: 457px; height: 301px; }
  .visual-one-day { background: linear-gradient(160deg, #e8ebf0 0%, #e8ebf0 30%, #f26b6b 48%, #ef4fa6 62%, #e8ebf0 80%); }
  .visual-special { background: linear-gradient(150deg, #ffffff 0%, #ffffff 25%, #fcd51a 45%, #ee3f8a 55%, #fcd51a 70%, #ffffff 90%); }
  .deal-text {
    margin-top: 16px; font-size: 13px; line-height: 23px; color: var(--body-ink);
  }
  .deal-link {
    display: inline-flex; align-items: center; gap: 3px;
    margin-top: 11px; font-size: 15px; font-weight: 700; color: var(--green);
    text-decoration: none; border-bottom: 1px solid var(--green); line-height: 17px;
  }
  .footer {
    position: absolute; top: 877px; left: 0; width: 1200px; height: 59px;
    background: var(--footer-bg); color: var(--footer-ink);
    font-size: 15px; display: flex; align-items: center; justify-content: center;
  }
</style>
</head>
<body>
  <div class="brand">LINQORA</div>
  <p class="tagline">CRAZY DAY SALE, SO GETS READY FOR YOUR WALLETS</p>
  <a class="cta-button cta-top" href="#">DAILY EMAILS SIGN UP</a>

  <section class="deal-card deal-left">
    <div class="deal-visual visual-one-day" role="img" aria-label="One day super sale banner: today only, save up to 50%"></div>
    <p class="deal-text">Sed ut perspiciatis unde omnis iste natus error sit volu accusantium doloremque laudantium, tot rem aperiam, eaque ipsa quae ab illo inventore veritatis et quasi architecto beatae vitae dicta sunt elicabo.</p>
    <a class="deal-link" href="#">CLICK HERE
      <svg width="12" height="12" viewBox="0 0 12 12" aria-hidden="true"><circle cx="6" cy="6" r="6" fill="#6cc552"/><path d="M3 6h4.5M5.5 3.5 8 6 5.5 8.5" stroke="#fff" stroke-width="1.6" fill="none" stroke-linecap="round" stroke-linejoin="round"/></svg>
    </a>
  </section>

  <section class="deal-card deal-right">
    <div class="deal-visual visual-special" role="img" aria-label="Sale special offer banner: 50% off"></div>
    <p class="deal-text">Sed ut perspiciatis unde omnis iste natus error sit volu accusantium doloremque laudantium, tot rem aperiam, eaque ipsa quae ab illo inventore veritatis et quasi architecto beatae vitae dicta sunt elicabo.</p>
    <a class="deal-link" href="#">CLICK HERE
      <svg width="12" height="12" viewBox="0 0 12 12" aria-hidden="true"><circle cx="6" cy="6" r="6" fill="#6cc552"/><path d="M3 6h4.5M5.5 3.5 8 6 5.5 8.5" stroke="#fff" stroke-width="1.6" fill="none" stroke-linecap="round" stroke-linejoin="round"/></svg>
    </a>
  </section>

  <a class="cta-button cta-bottom" href="#">DAILY EMAILS SIGN UP</a>

  <footer class="footer">© 2021 Linqora. All Rights Reserved.</footer>
</body>
</html>
```